VORLAX POSTCARD

I submitted my postcard and printer said it is not acceptable here are the comments
Item 125301 - Front file: Uploaded png is 3.3 x 2.2" at 300 dpi. Back file: Uploaded png is 5 x 3.3" at 200 dpi. There is text and images too close to the edges for the front and back. Both front/back files are low resolution and have poor print quality. The correct size for a jumbo postcard is 8.75 x 5.75". The intended bleed extends to the edges and all important text and/or elements are to remain at least 3/8" away from the edges. Try saving as a PDF from the source file at the correct size for a possible better printing output.

Item 125302 - Front file: Uploaded jpg is 7 x 5" at 200 dpi. Back file: Uploaded jpg is 8 x 5" at 220 dpi. Both front/back files are low resolution and have poor print quality. The correct size for a Medium QTVR card is 8.25 x 6.75" The intended bleed extends to the edges of the canvas and all important text and/or elements are to remain at least 3/8" away from the edges. Try saving as a PDF from the source file at the correct size for a possible better printing output.

```html
<!DOCTYPE html>
<html lang="en">
<head>
<meta charset="utf-8">
<title>Vorlax Postcard</title>
<link href="https://fonts.googleapis.com/css2?family=Oswald:wght@600&family=Titillium+Web:wght@400;600;700&family=Open+Sans:wght@400;600&display=swap" rel="stylesheet">
<style>
  :root {
    --blue: #0d62a8;
    --yellow: #f7bd2b;
    --yellow-deep: #f2b01c;
    --ink: #1c1c1c;
    --white: #ffffff;
    --backdrop: #7b7b7b;
    --red: #c8242b;
    --badge: #dfe6ee;
  }
  * { margin: 0; padding: 0; box-sizing: border-box; }
  html, body { width: 1200px; height: 904px; overflow: hidden; }
  body { background: var(--backdrop); position: relative; font-family: "Open Sans", sans-serif; color: var(--ink); }

  .card { position: absolute; width: 480px; height: 392px; background: var(--white); overflow: hidden; box-shadow: 0 6px 18px rgba(0,0,0,.35); }
  .card--front { left: 193px; top: 41px; }
  .card--back { left: 482px; top: 470px; }

  .abs { position: absolute; }
  .brand { font-family: "Titillium Web", sans-serif; font-weight: 600; color: var(--blue); display: flex; align-items: center; gap: 6px; line-height: 1; white-space: nowrap; }
  .brand__dot { width: 12px; height: 12px; border-radius: 50%; background: var(--yellow); }

  /* front */
  .front__header { left: 0; top: 0; width: 480px; height: 90px; background: linear-gradient(115deg, #f4f4f4, #ffffff 60%, #ececec); }
  .front__brand { left: 26px; top: 34px; font-size: 34px; }
  .front__brand .brand__dot { width: 14px; height: 14px; }
  .front__band { left: 0; top: 90px; width: 480px; height: 73px; background: var(--blue); }
  .front__team { left: 212px; top: 0; width: 268px; height: 163px; }
  .front__headline { left: 26px; top: 103px; font-family: "Oswald", sans-serif; font-weight: 600; font-size: 17px; line-height: 23px; color: var(--yellow); text-transform: uppercase; white-space: nowrap; z-index: 1; }
  .front__features { left: 0; top: 163px; width: 480px; height: 117px; background: linear-gradient(120deg, var(--yellow-deep), var(--yellow) 55%, #f9c844); }
  .feature { position: absolute; display: flex; gap: 4px; font-family: "Titillium Web", sans-serif; font-weight: 700; font-size: 9.6px; line-height: 11.5px; color: var(--ink); text-transform: uppercase; }
  .feature__mark { flex: none; width: 9px; height: 9px; margin-top: 1px; border-radius: 50%; border: 1.6px solid var(--blue); background: radial-gradient(circle, var(--blue) 0 2px, transparent 2.4px); }
  .feature__note { display: block; font-weight: 400; font-size: 6.2px; line-height: 8px; text-transform: none; }
  .front__partners { left: 0; top: 279px; width: 480px; height: 71px; background: var(--white); }
  .badge { position: absolute; height: 12px; border-radius: 3px; background: var(--badge); }
  .cash { left: 412px; top: 293px; font-family: "Titillium Web", sans-serif; font-weight: 600; font-size: 7.2px; line-height: 9px; color: var(--red); text-align: center; }
  .front__footer { left: 0; top: 350px; width: 480px; height: 42px; background: var(--blue); display: flex; align-items: center; gap: 11px; padding-left: 26px; color: var(--white); font-family: "Titillium Web", sans-serif; font-size: 10px; white-space: nowrap; }
  .front__footer strong { font-weight: 700; }
  .contact { display: flex; align-items: center; gap: 4px; font-weight: 600; white-space: nowrap; }
  .contact svg { width: 9px; height: 9px; flex: none; }

  /* back */
  .back__panel { left: 0; top: 0; width: 480px; height: 392px; }
  .back__tagline { left: 26px; top: 24px; font-family: "Titillium Web", sans-serif; font-weight: 700; font-size: 12px; line-height: 16px; color: var(--yellow); text-transform: uppercase; }
  .back__doctor { left: 26px; top: 81px; font-family: "Oswald", sans-serif; font-weight: 600; font-size: 13px; color: var(--blue); white-space: nowrap; }
  .back__portrait { left: 153px; top: 21px; width: 94px; height: 94px; border-radius: 50%; border: 4px solid var(--white); background: radial-gradient(circle at 50% 40%, #d9c3b0, #8fc8c9 75%); }
  .back__heading { left: 26px; top: 111px; font-family: "Titillium Web", sans-serif; font-weight: 700; font-size: 10.6px; line-height: 13.5px; color: var(--blue); text-transform: uppercase; white-space: nowrap; }
  .back__bio { left: 26px; top: 139px; width: 206px; font-size: 6.5px; line-height: 9px; text-align: justify; }
  .back__bio p + p { margin-top: 5px; text-align: left; }
  .back__services-title { left: 27px; top: 259px; font-family: "Titillium Web", sans-serif; font-weight: 700; font-size: 9.4px; color: var(--blue); text-transform: uppercase; white-space: nowrap; }
  .services { position: absolute; list-style: none; font-family: "Titillium Web", sans-serif; font-weight: 600; font-size: 7px; line-height: 13px; white-space: nowrap; }
  .services li { display: flex; align-items: center; gap: 4px; }
  .services li::before { content: ""; width: 6px; height: 6px; border-radius: 50%; background: var(--blue); box-shadow: inset 0 0 0 1.5px var(--blue), inset 0 0 0 2.4px var(--white); }
  .services--left { left: 27px; top: 272px; }
  .services--right { left: 97px; top: 272px; }
  .back__footer { left: 26px; top: 365px; display: flex; gap: 9px; color: var(--white); font-family: "Titillium Web", sans-serif; font-size: 9px; }
  .back__brand { left: 280px; top: 36px; font-size: 20px; }
  .back__brand .brand__dot { width: 9px; height: 9px; }
  .back__return { left: 292px; top: 66px; font-family: "Titillium Web", sans-serif; font-weight: 600; font-size: 7px; line-height: 9px; white-space: nowrap; }
  .indicia { left: 386px; top: 26px; width: 68px; height: 67px; border: 1px solid #9a9a9a; font-size: 5.6px; line-height: 7.4px; text-align: center; padding-top: 19px; }
  .indicia b { font-weight: 600; }
  .indicia small { font-size: 3.8px; display: block; }
  .mailbox { left: 292px; top: 104px; width: 133px; height: 36px; border: 1px solid #9a9a9a; font-size: 5.6px; padding: 5px 7px; }
  .mailbox__route { text-align: center; }
  .mailbox__name { margin-top: 9px; }
</style>
</head>
<body>

<section class="card card--front" aria-label="Postcard front">
  <div class="abs front__header"></div>
  <div class="abs brand front__brand"><span class="brand__dot"></span>Vorlax</div>
  <div class="abs front__band"></div>

  <svg class="abs front__team" viewBox="0 0 268 163" role="img" aria-label="Group photo of the clinic's doctors and nurses in scrubs and white coats">
    <defs>
      <linearGradient id="teamTone" x1="0" y1="0" x2="1" y2="1">
        <stop offset="0" stop-color="#e7ecf1"/>
        <stop offset=".55" stop-color="#9fb2c6"/>
        <stop offset="1" stop-color="#3f5f86"/>
      </linearGradient>
    </defs>
    <path d="M40 30 C80 8 180 8 268 28 L268 22 C180 0 80 0 32 26 Z" fill="var(--yellow)"/>
    <path d="M56 36 C114 16 200 18 268 36 L268 163 L40 163 C14 130 20 70 56 36 Z" fill="url(#teamTone)"/>
    <path d="M56 36 C20 70 14 130 40 163 L32 163 C4 128 10 66 48 32 Z" fill="var(--blue)"/>
  </svg>
  <h1 class="abs front__headline">Primary care medicine<br>right on Linden</h1>

  <div class="abs front__features">
    <div class="feature" style="left:26px;top:22px"><span class="feature__mark"></span><span>All insurances accepted including<br>Medicare/Medicaid</span></div>
    <div class="feature" style="left:26px;top:53px"><span class="feature__mark"></span><span>Accepting new patients/immediate<br>appointment available</span></div>
    <div class="feature" style="left:26px;top:87px"><span class="feature__mark"></span><span>First-class state of the art office</span></div>
    <div class="feature" style="left:242px;top:22px;width:212px"><span class="feature__mark"></span><span>Be seen by board certified internal medicine doctor <span class="feature__note" style="display:inline">(The doctor will be available when you need her. No shuffling from doctor-to-doctor Or. Haskett will be YOUR doctor)</span></span></div>
    <div class="feature" style="left:242px;top:64px"><span class="feature__mark"></span><span>Multiple specialists under one roof<span class="feature__note">(Psychiatry, Podiatry, Chiropractic, Cardiology, Pain Management)</span></span></div>
    <div class="feature" style="left:242px;top:89px"><span class="feature__mark"></span><span>On site blood laboratory</span></div>
  </div>

  <div class="abs front__partners">
    <span class="badge" style="left:26px;top:12px;width:62px"></span>
    <span class="badge" style="left:94px;top:14px;width:50px"></span>
    <span class="badge" style="left:150px;top:12px;width:54px"></span>
    <span class="badge" style="left:214px;top:15px;width:30px"></span>
    <span class="badge" style="left:252px;top:15px;width:54px"></span>
    <span class="badge" style="left:314px;top:15px;width:48px"></span>
    <span class="badge" style="left:368px;top:15px;width:38px"></span>
    <span class="badge" style="left:26px;top:42px;width:48px"></span>
    <span class="badge" style="left:84px;top:42px;width:36px"></span>
    <span class="badge" style="left:128px;top:42px;width:50px"></span>
    <span class="badge" style="left:184px;top:42px;width:46px"></span>
    <span class="badge" style="left:234px;top:44px;width:48px"></span>
    <span class="badge" style="left:288px;top:44px;width:42px"></span>
    <span class="badge" style="left:336px;top:42px;width:46px"></span>
    <span class="badge" style="left:392px;top:42px;width:54px"></span>
  </div>
  <p class="abs cash">CASH<br>PATIENTS<br>WELCOME</p>

  <footer class="abs front__footer">
    <strong>CALL US TODAY!</strong>
    <span class="contact"><svg viewBox="0 0 10 10"><circle cx="5" cy="5" r="5" fill="var(--yellow)"/><path d="M3 2.6 l1 1 -0.5 .7 a3.4 3.4 0 0 0 1.5 1.5 l.7-.5 1 1 -.8.9 C4.5 7 3 5.5 2.3 3.4Z" fill="var(--blue)"/></svg>555-014-2290</span>
    <span class="contact"><svg viewBox="0 0 10 10"><circle cx="5" cy="5" r="5" fill="var(--yellow)"/><rect x="2.5" y="3.2" width="5" height="3.6" fill="none" stroke="var(--blue)" stroke-width=".8"/><path d="M2.5 3.4 L5 5.3 7.5 3.4" fill="none" stroke="var(--blue)" stroke-width=".8"/></svg>care@vorlaxclinic.com</span>
    <span class="contact"><svg viewBox="0 0 10 10"><circle cx="5" cy="5" r="5" fill="var(--yellow)"/><circle cx="5" cy="5" r="2.8" fill="none" stroke="var(--blue)" stroke-width=".7"/><path d="M2.2 5h5.6M5 2.2c-1.4 1.6-1.4 4 0 5.6M5 2.2c1.4 1.6 1.4 4 0 5.6" fill="none" stroke="var(--blue)" stroke-width=".6"/></svg>www.harrowbrookmedia.com</span>
  </footer>
</section>

<section class="card card--back" aria-label="Postcard back">
  <svg class="abs back__panel" viewBox="0 0 480 392" aria-hidden="true">
    <path d="M0 0 H240 C262 40 264 70 262 76 H0 Z" fill="var(--blue)"/>
    <path d="M0 78 H262 C261 88 258 96 256 103 H0 Z" fill="var(--yellow)"/>
    <path d="M248 0 H262 C286 60 268 170 240 250 C222 300 218 340 250 392 H236 C204 340 212 300 230 250 C258 170 272 60 248 0 Z" fill="var(--yellow)"/>
    <path d="M0 353 H230 C236 368 244 382 254 392 H0 Z" fill="var(--blue)"/>
    <path d="M262 176 C238 250 226 320 270 392 H260 C218 320 230 250 256 180 Z" fill="var(--blue)"/>
    <rect x="270" y="385" width="210" height="7" fill="var(--yellow)"/>
  </svg>

  <p class="abs back__tagline">Se' habla espanol<br>tele-visits<br>available</p>
  <p class="abs back__doctor">Lenora Haskett, MD</p>
  <div class="abs back__portrait" role="img" aria-label="Portrait photo of Dr. Lenora Haskett"></div>

  <h2 class="abs back__heading">A doctor who<br>cares experience you can trust</h2>
  <div class="abs back__bio">
    <p>Dr. Haskett has been practicing medicine in Marlow for over 12 years. She was previously a primary care doctor with St. Brennan Riverside Clinic in Marlow for 10 years. Dr. Haskett became dissatisfied with the assembly line fashion of medical care and the pressure to spend minimal time with patients. Dr. Haskett choose to go out on her own to deliver medical care the way she believes it should be practiced. Dr. Haskett prides herself on delivering the individual care that patients require no matter the time required.</p>
    <p>Dr. Haskett maintains hospital privileges at Halden/St. Brennan of Linden, Corwell, Ashby.</p>
  </div>

  <h3 class="abs back__services-title">All primary care services including</h3>
  <ul class="services services--left">
    <li>Diabetes</li><li>Colds</li><li>Flu</li><li>COVID</li><li>Sports Physicals</li><li>Blood Tests</li>
  </ul>
  <ul class="services services--right">
    <li>Hypertension (High Blood Pressure)</li><li>Auto Accidents/Slip &amp; Fall</li><li>Back /Neck /Knee /Shoulder PAIN</li><li>Vaccinations for Flu, Pneumonia</li><li>Immigration examinations</li><li>Social Security Examinations</li>
  </ul>

  <footer class="abs back__footer">
    <span class="contact"><svg viewBox="0 0 10 10"><circle cx="5" cy="5" r="5" fill="var(--yellow)"/><path d="M3 2.6 l1 1 -0.5 .7 a3.4 3.4 0 0 0 1.5 1.5 l.7-.5 1 1 -.8.9 C4.5 7 3 5.5 2.3 3.4Z" fill="var(--blue)"/></svg>555-014-2290</span>
    <span class="contact"><svg viewBox="0 0 10 10"><circle cx="5" cy="5" r="5" fill="var(--yellow)"/><circle cx="5" cy="5" r="2.8" fill="none" stroke="var(--blue)" stroke-width=".7"/><path d="M2.2 5h5.6M5 2.2c-1.4 1.6-1.4 4 0 5.6M5 2.2c1.4 1.6 1.4 4 0 5.6" fill="none" stroke="var(--blue)" stroke-width=".6"/></svg>www.harrowbrookmedia.com</span>
  </footer>

  <div class="abs brand back__brand"><span class="brand__dot"></span>Vorlax</div>
  <p class="abs back__return">418 LINDEN AVENUE<br>MARLOW, NJ 08210</p>
  <div class="abs indicia">PRSRT MKTG<br>U.S. POSTAGE<br><b>PAID</b><small>PARCELGROVECARDS.COM</small></div>
  <div class="abs mailbox">
    <p class="mailbox__route">*********ECRWSSQTVR****</p>
    <p class="mailbox__name">Postal Customer</p>
  </div>
</section>

</body>
</html>
```